Medical Billing Company Needs a Business Card Design

We need a business card design for a Florida based medical billing company called 'Medora Crestline Solutions'. We specialize in providing revenue cycle management services to physician and therapist offices (we're basically their back-office processing partner for providing billing software, claims submissions, A/R follow-up and patient statements & collections. Our logo is red and blue-ish, so make sure that whatever other elements are used will match appropriately. Our current business card design has a too small font size. I'd like to project an image that shows we are modern & reliable. On a side note, I'm planning on using ZIB for printing these cards.

Target Market(s)

Office managers, physicians, therapists

Industry/Entity Type

Printing

Requirements
Must have
• Logo
Name of Employee
Phone
Fax
E-mail
Website

```html
<!DOCTYPE html>
<html lang="en">
<head>
<meta charset="utf-8">
<title>Medora Crestline Solutions – Business Card</title>
<link href="https://fonts.googleapis.com/css2?family=Source+Sans+3:wght@400;600&display=swap" rel="stylesheet">
<style>
  :root {
    --navy: #2f2a72;
    --red: #a3161f;
    --grey: #5e5e5e;
    --white: #ffffff;
    --black: #050505;
    --stage: #3b332d;
    --dark-mark: #6a63b8;
    --light-url: #d0d0d0;
  }
  * { margin: 0; padding: 0; box-sizing: border-box; }
  html, body { width: 1200px; height: 844px; overflow: hidden; }
  body {
    background: var(--stage);
    font-family: "Source Sans 3", sans-serif;
    position: relative;
  }
  .card {
    position: absolute;
    width: 484px;
    height: 276px;
    background: var(--white);
    box-shadow: 0 6px 14px rgba(0,0,0,.45);
    overflow: hidden;
  }
  .card--front { left: 69px; top: 112px; }
  .card--back-one { left: 597px; top: 112px; }
  .card--back-two { left: 69px; top: 417px; }
  .card--back-three { left: 599px; top: 418px; background: var(--black); }

  .wordmark {
    font-weight: 600;
    color: var(--navy);
    letter-spacing: 1.5px;
    white-space: nowrap;
  }
  .card--front .wordmark {
    position: absolute; left: 28px; top: 28px; font-size: 29px;
  }

  .company-details {
    position: absolute; left: 29px; top: 165px;
    font-size: 12.5px; line-height: 15px; color: var(--grey);
  }
  .phone-line {
    position: absolute; left: 29px; top: 212px;
    font-size: 12px; color: var(--red); word-spacing: 2px;
  }
  .phone-line span + span { margin-left: 14px; }

  .employee {
    position: absolute; left: 330px; top: 168px; width: 110px;
    text-align: center;
  }
  .employee-name { font-size: 19px; color: var(--red); font-weight: 600; line-height: 22px; }
  .employee-role { font-size: 13px; color: var(--red); }

  .contact-band {
    position: absolute; left: 0; bottom: 0; width: 484px; height: 24px;
  }
  .band-text {
    position: absolute; bottom: 4px;
    font-size: 12.5px; color: var(--white);
  }
  .band-email { left: 29px; }
  .band-email b { font-weight: 600; }
  .band-web { left: 286px; }

  .back-lockup {
    position: absolute; left: 0; right: 0; top: 50%;
    transform: translateY(-50%);
    text-align: center;
  }
  .back-lockup .wordmark { font-size: 30px; display: block; }
  .back-lockup .url {
    font-size: 12px; color: #444; letter-spacing: 1px; margin-top: 2px; display: block;
  }
  .card--back-three .wordmark { color: var(--dark-mark); }
  .card--back-three .url { color: var(--light-url); }

  .label {
    position: absolute; font-size: 33px; color: var(--white); font-weight: 400;
  }
  .label--one { left: 960px; top: 50px; }
  .label--two { left: 106px; top: 728px; }
  .label--three { left: 997px; top: 724px; }
</style>
</head>
<body>

  <div class="label label--one">Back 1</div>

  <section class="card card--front" aria-label="Card front">
    <div class="wordmark">MEDORA CRESTLINE</div>

    <p class="company-details">
      Medora Crestline Solutions, Inc<br>
      2180 SE Harbor Lane, Coral Bend, FL 34120
    </p>
    <p class="phone-line"><span>P: 555 214 0387</span><span>F: 555 214 0388</span></p>

    <div class="employee">
      <div class="employee-name">Yourname</div>
      <div class="employee-role">Director</div>
    </div>

    <svg class="contact-band" viewBox="0 0 484 24" preserveAspectRatio="none" aria-hidden="true">
      <polygon points="0,0 275,0 265,24 0,24" fill="var(--navy)"/>
      <polygon points="279,0 484,0 484,24 269,24" fill="var(--red)"/>
    </svg>
    <span class="band-text band-email"><b>Email:</b> hello@medoracrestline.net</span>
    <span class="band-text band-web">www.medoracrestline.net</span>
  </section>

  <section class="card card--back-one" aria-label="Card back, option one">
    <div class="back-lockup">
      <span class="wordmark">MEDORA CRESTLINE</span>
      <span class="url">www.medoracrestline.net</span>
    </div>
  </section>

  <section class="card card--back-two" aria-label="Card back, option two">
    <div class="back-lockup">
      <span class="wordmark">MEDORA CRESTLINE</span>
      <span class="url">www.medoracrestline.net</span>
    </div>
  </section>

  <section class="card card--back-three" aria-label="Card back, option three">
    <div class="back-lockup">
      <span class="wordmark">MEDORA CRESTLINE</span>
      <span class="url">www.medoracrestline.net</span>
    </div>
  </section>

  <div class="label label--two">Back 2</div>
  <div class="label label--three">Back 3</div>

</body>
</html>
```